Medical Education and Learning Portal refresh

We at uVeldra Limited have developed a learning platform for medical students. It is based around multiple choice questions, but has social and gaming elements built in to make it fun. It will be used on desktop and mobile devices.

I am looking for a refresh of the 'dated' design into something modern and transferrable between devices.

Note that I have a 'focus group' of Medical Students on 4 February where the Top 3-4 designs will be shown to them for them to pick the winner.

I have also uploaded screenshots of the current site. Essentially I would like to reduce the complexity of design into 2-3 pages (currently unlogged in front/home page, logged in page with options, answer questions page, competition page, revision page/summary pages etc). What I am really after is a good clean colour scheme & structure.

If we get the design colour scheme right then I can pay additionally for coding and maybe some additional structure to pages.
Updates

Target Market(s)

Healthcare/Medical Students

Industry/Entity Type

Healthcare

Number of Pages Required

4 page

Font styles to use
Serif
Sans Serif

Requirements
Must have
• 'Clean' Web 2.0 (or later) feel to it.
• I also expect that the images for the trophies are 'cleaned up (each trophy has a bronze/silver/platinum version as users increase their score. I am looking for these to be clean and simple but fun!
• I also need the final design to be transferrable from a desktop browser to a mobile device. I will need designs for home page/content page/Q&A page.
• I previously had a side panel float over the site but that is dated now and I would like to have a page with each element clearly on it and any information would briefly float over this but not take the focus away from the main function of the page.
• I have included the 'bronze', 'silver', 'gold' trophy icons in the files. These are fine in one sense but ideally the colours will blend well too ...
• The following article summarises my must haves:
• http://pagecraftnotes.example/web-design/web-2-0-design-style-guide/
Nice to have
• Creative concept for presenting MCQ's to students, with a timer and box of information about the question (level of the question, the percent of student who get it right ... etc).
Should not have
• Too much complexity ... clean with a few colours is what I am after
• Note too that my logo is not changing and the colours should blend with this.

```html
<!DOCTYPE html>
<html lang="en">
<head>
<meta charset="utf-8">
<title>uVeldra — The Medical Peer Review</title>
<link rel="stylesheet" href="https://fonts.googleapis.com/css2?family=Lato:ital,wght@0,300;0,400;0,700;1,400&family=Roboto:wght@400;500&display=swap">
<style>
:root{
  --page-bg:#e6e7ea;
  --sheet:#ffffff;
  --navy:#3d5a78;
  --slate:#4c6a8a;
  --slate-dark:#3f5973;
  --orange:#f7941d;
  --sky:#1fb2e6;
  --sky-dark:#0f8fc6;
  --ink:#444a52;
  --muted:#6b7280;
  --rule:#e3e5e8;
  --panel:#f0f1f3;
  --link:#2a9fd8;
}
*{box-sizing:border-box;margin:0;padding:0}
html,body{width:908px;height:1200px;overflow:hidden}
body{background:var(--page-bg);font-family:'Roboto',sans-serif;color:var(--ink);position:relative}
.abs{position:absolute}
.brand{left:48px;top:22px}
.brand-name{font-family:'Lato',sans-serif;font-weight:400;font-size:30px;color:var(--slate);line-height:1}
.brand-tag{font-family:'Roboto',sans-serif;font-size:9px;font-weight:500;color:var(--navy);margin-top:6px}
.login{left:781px;top:34px;width:70px;height:26px;background:var(--orange);color:#fff;font-size:11px;display:flex;align-items:center;justify-content:center;border-radius:2px}
.sheet{left:46px;top:91px;width:816px;height:1081px;background:var(--sheet);border-top:2px solid var(--slate)}
.nav{left:46px;top:93px;height:51px;width:816px;display:flex;border-bottom:2px solid var(--rule)}
.nav a{display:flex;align-items:center;justify-content:center;font-size:11.5px;color:var(--navy);text-decoration:none;border-right:1px solid var(--rule)}
.nav a.active{color:var(--orange)}
.nav .more{border-right:none;font-size:18px;letter-spacing:1px;font-weight:500}
.hero-photo{left:56px;top:160px;width:493px;height:308px;background:linear-gradient(100deg,#c9d2da 0%,#e9edf1 45%,#f4f6f8 100%)}
.hero-panel{left:549px;top:160px;width:303px;height:308px;background:var(--slate);color:#fff;padding:45px 0 0 29px}
.hero-panel h1{font-family:'Lato',sans-serif;font-weight:400;font-size:24px;line-height:1.1}
.hero-panel h2{font-family:'Lato',sans-serif;font-weight:400;font-size:19px;margin-top:6px}
.hero-panel ul{list-style:none;margin-top:16px}
.hero-panel li{font-family:'Lato',sans-serif;font-style:italic;font-size:12px;line-height:21px;position:relative;padding-left:14px}
.hero-panel li:before{content:"";position:absolute;left:0;top:8px;width:4px;height:4px;border-radius:50%;background:#fff}
.btn-outline{display:inline-flex;width:124px;height:33px;border:2px solid #fff;border-radius:2px;align-items:center;justify-content:center;font-family:'Lato',sans-serif;font-size:12px;margin-top:20px}
.dots{left:763px;top:426px;display:flex;gap:4px}
.dots span{width:10px;height:10px;border-radius:50%;background:#3b5673}
.dots span:first-child{background:#fff}
.section-title{font-family:'Lato',sans-serif;font-weight:400;color:var(--navy);text-transform:uppercase}
.peers-title{left:62px;top:528px;font-size:20px}
.peers-copy{left:62px;top:566px;width:584px;font-family:'Lato',sans-serif;font-size:11px;line-height:17px;color:#4a4f55}
.btn-solid{left:62px;top:651px;width:115px;height:32px;background:linear-gradient(#5d7c99,#486683);color:#fff;font-family:'Lato',sans-serif;font-size:12px;display:flex;align-items:center;justify-content:center;border-radius:2px}
.peers-art{left:667px;top:566px;width:183px;height:144px;background:linear-gradient(#f2f4f6 0%,#3d83c8 75%)}
.divider{left:56px;top:710px;width:796px;height:1px;background:var(--rule)}
.video{left:62px;top:752px;width:297px;height:238px;background:#000}
.video-head{height:29px;display:flex;align-items:center;justify-content:space-between;padding:0 10px;color:#fff;font-size:11.5px}
.video-thumb{position:absolute;left:0;top:29px;width:297px;height:180px;background:radial-gradient(circle at 50% 50%,#fff 0%,#fae06a 45%,#f5d20c 100%);display:flex;align-items:center;justify-content:center}
.feed-title{font-size:17px}
.tw{left:381px;top:757px;width:212px}
.tw-item{display:flex;gap:14px;padding:16px 0 14px;border-bottom:1px solid var(--rule)}
.tw-item:last-of-type{border-bottom:none}
.tw-dot{flex:0 0 25px;height:25px;border-radius:50%;background:var(--link)}
.tw-item p{font-size:11px;line-height:15.5px;text-align:justify;color:#4a4f55}
.tw-item em{color:var(--link)}
.view-all{font-family:'Lato',sans-serif;font-style:italic;font-size:11.5px}
.fb{left:619px;top:751px;width:233px;height:239px;background:var(--panel);padding:18px 16px}
.fb-item{display:flex;gap:13px;margin-top:18px}
.avatar{flex:0 0 47px;height:47px;background:linear-gradient(#c7a47a,#8c7b6c)}
.fb-item p{font-family:'Lato',sans-serif;font-size:10.5px;line-height:15.5px;text-align:justify;color:#4a4f55}
.newsletter{left:46px;top:1040px;width:816px;height:60px;background:var(--sky);display:flex;align-items:center;padding-left:25px;color:#fff}
.newsletter h3{font-family:'Lato',sans-serif;font-weight:400;font-size:17px;margin-left:14px;width:171px}
.field{width:171px;height:25px;border:1px solid #fff;font-size:9px;display:flex;align-items:center;padding-left:13px;margin-right:13px}
.subscribe{width:126px;height:28px;background:var(--sky-dark);font-size:11px;display:flex;align-items:center;justify-content:center;margin-left:4px}
.foot-links{left:62px;top:1120px;font-size:11px;color:#555}
.foot-copy{left:62px;top:1140px;font-size:11px;color:#555}
.social{left:657px;top:1119px;display:flex;gap:9px}
.social span{width:30px;height:30px;border-radius:50%;background:var(--slate-dark)}
</style>
</head>
<body>
<div class="abs brand"><div class="brand-name">uVeldra</div><div class="brand-tag">The Medical Peer Review</div></div>
<div class="abs login">LOGIN</div>
<div class="abs sheet"></div>
<nav class="abs nav">
  <a class="active" style="width:78px">Home</a>
  <a style="width:100px">Take the tour</a>
  <a style="width:129px">What your peers say</a>
  <a style="width:125px">Subscription Plans</a>
  <a style="width:92px">Free signup</a>
  <a style="width:91px">Contact Us</a>
  <a style="width:93px">Moderation</a>
  <a style="width:67px">Statiscs</a>
  <a class="more" style="width:41px">•••</a>
</nav>
<div class="abs hero-photo" role="img" aria-label="Photo of a doctor holding a stethoscope toward the viewer"></div>
<div class="abs hero-panel">
  <h1>UVELDRA</h1>
  <h2>THE MEDICAL PEER REVIEW</h2>
  <ul>
    <li>Write study pages for complex questions</li>
    <li>Review your peers study pages</li>
    <li>Revise your study pages for exams</li>
  </ul>
  <div class="btn-outline">READ MORE</div>
</div>
<div class="abs dots"><span></span><span></span><span></span><span></span></div>
<h2 class="abs section-title peers-title">What your peers say</h2>
<p class="abs peers-copy">Lorem ipsum dolor sit amet, consectetur adipiscing elit, sed do eiusmod tempor incididunt ut labore et dolore magna aliqua. Ut enim ad minim veniam, quis nostrud exercitation ullamco laboris nisi ut aliquip ex ea commodo consequat. Duis aute irure dolor in reprehenderit in voluptate velit esse cillum dolore eu fugiat nulla pariatur. Excepteur sint occaecat cupidatat non proident, sunt in culpa qui officia deserunt mollit anim id est laborum.</p>
<div class="abs btn-solid">READ MORE</div>
<div class="abs peers-art" role="img" aria-label="Illustration of a female and a male medical professional in blue"></div>
<div class="abs divider"></div>
<div class="abs video">
  <div class="video-head"><span>uVeldra Landing Video</span>
    <svg width="34" height="12" viewBox="0 0 34 12"><circle cx="6" cy="6" r="5.5" fill="#fff"/><path d="M6 3v3h2.5" stroke="#000" stroke-width="1.3" fill="none"/><path d="M20 10c1-4 4-6 9-6V1l5 4.5L29 10V7c-4 0-7 1-9 3z" fill="#fff"/></svg>
  </div>
  <div class="video-thumb" role="img" aria-label="Video still: laptop and devices on a yellow splash">
    <svg width="42" height="30" viewBox="0 0 42 30"><rect width="42" height="30" rx="6" fill="#222"/><path d="M17 9l10 6-10 6z" fill="#fff"/></svg>
  </div>
</div>
<div class="abs tw">
  <h3 class="section-title feed-title">Chirpline Feed</h3>
  <div class="tw-item"><span class="tw-dot"></span><p>Lorem ipsum <em>dolor@sit amet,</em> consectetur adipiscing elit, sed do eiusmod tempor incididunt ut labore et dolore</p></div>
  <div class="tw-item"><span class="tw-dot"></span><p>Lorem ipsum <em>dolor@sit amet,</em> consectetur adipiscing elit, sed do eiusmod tempor incididunt ut labore et dolore</p></div>
  <div class="view-all" style="color:var(--slate);margin-top:2px">view all feed</div>
</div>
<div class="abs fb">
  <h3 class="section-title feed-title">Friendboard Feed</h3>
  <div class="fb-item"><span class="avatar" role="img" aria-label="Profile photo"></span><p>Excepteur sint occaecat cupid atat non proident, sunt in culpa qui officia deserunt mollit anim id est.</p></div>
  <div class="fb-item" style="margin-top:24px"><span class="avatar" role="img" aria-label="Profile photo"></span><p>Excepteur sint occaecat cupid atat non proident, sunt in culpa qui officia.</p></div>
  <div class="view-all" style="color:var(--orange);margin-top:14px">view all feed</div>
</div>
<div class="abs newsletter">
  <svg width="28" height="20" viewBox="0 0 28 20"><rect x="1" y="1" width="26" height="18" fill="none" stroke="#fff" stroke-width="1.5"/><path d="M1 1l13 10L27 1M1 19l10-9M27 19l-10-9" fill="none" stroke="#fff" stroke-width="1.5"/></svg>
  <h3>Newsletter Sign Up</h3>
  <div class="field">ENTER NAME</div>
  <div class="field">ENTER EMAIL</div>
  <div class="subscribe">SUBSCRIBE</div>
</div>
<div class="abs foot-links">Home &nbsp;| &nbsp;Take The Tour &nbsp;| &nbsp;What your peers say &nbsp;| &nbsp;Subscription Plans &nbsp;&nbsp;| Free Signup</div>
<div class="abs foot-copy">© 2016 uVeldra Limited | All rights reserved.</div>
<div class="abs social"><span></span><span></span><span></span><span></span><span></span></div>
</body>
</html>
```